New Business Cards for MB&LR

We need updated business cards for a staff of 15 engineers, estimators, project managers, and sales people. We have recently begun changes to our website and marketing material to improve our look and branding. We are an established fabricator specializing in pressure vessels, tanks, and structural steel. The owners require us to use the existing logo and old english text design. Also, we prefer dark grey or mostly black cards.
Target Market(s)
Engineers, purchasing agents, estimators, and project managers of; mining companies, refineries, industrial construction professionals
Industry/Entity Type
Business
Contact Information for Business Card
Logo, phone, website, email, etc.
Look and feel

```html
<!DOCTYPE html>
<html lang="en">
<head>
<meta charset="utf-8">
<title>MB&amp;LR Business Card</title>
<link rel="stylesheet" href="https://fonts.googleapis.com/css2?family=UnifrakturMaguntia&family=Old+Standard+TT:wght@400;700&family=Open+Sans:wght@400;600;700&display=swap">
<style>
  :root {
    --page-bg: #e9e7e4;
    --card-white: #fbfbfa;
    --ink: #1a1a1a;
    --ink-soft: #3a3a3a;
    --back-dark: #0f1620;
    --back-mid: #2a3647;
    --back-haze: #55606e;
    --back-text: #f2f2f2;
    --badge: #1a1a1a;
  }
  * { box-sizing: border-box; margin: 0; padding: 0; }
  html, body {
    width: 1200px; height: 844px; overflow: hidden;
    background: var(--page-bg);
  }
  .canvas {
    position: relative; width: 1200px; height: 844px;
    display: flex; align-items: center; justify-content: center; gap: 60px;
  }
  .card {
    position: relative; width: 520px; height: 297px;
    box-shadow: 0 6px 18px rgba(0,0,0,0.18);
    overflow: hidden;
  }

  /* Front */
  .card-front { background: var(--card-white); color: var(--ink); }
  .cert-badge { position: absolute; left: 22px; top: 70px; }
  .anniversary-badge { position: absolute; right: 34px; top: 50px; }
  .brand-mark {
    position: absolute; left: 0; right: 0; top: 40px;
    display: flex; align-items: center; justify-content: center; gap: 8px;
    font-family: "Old Standard TT", serif; font-weight: 700;
    font-size: 26px; color: var(--ink);
  }
  .brand-mark .mark-square { width: 14px; height: 14px; background: var(--ink); }
  .company-line {
    position: absolute; left: 170px; right: 110px; top: 96px;
    font-family: "UnifrakturMaguntia", serif; font-size: 18px;
    text-align: center; padding-bottom: 3px;
    border-bottom: 1px solid var(--ink);
  }
  .contact { position: absolute; left: 30px; top: 170px; }
  .contact .person-name {
    font-family: "Old Standard TT", serif; font-weight: 700; font-size: 22px;
  }
  .contact .person-title {
    font-family: "Open Sans", sans-serif; font-size: 12px; color: var(--ink-soft);
    margin-top: 1px;
  }
  .contact .address, .contact .phones {
    font-family: "Open Sans", sans-serif; font-size: 11.5px; color: var(--ink-soft);
  }
  .contact .address { margin-top: 14px; }
  .contact .phones { margin-top: 10px; }
  .contact .phones b { font-weight: 700; color: var(--ink); }
  .contact .web { font-weight: 700; color: var(--ink); }

  /* Back */
  .card-back {
    background: radial-gradient(ellipse at 70% 45%, var(--back-haze) 0%, var(--back-mid) 40%, var(--back-dark) 100%);
  }
  .card-back .scene-fill { position: absolute; inset: 0; }
  .back-title {
    position: absolute; left: 40px; right: 40px; top: 150px;
    font-family: "UnifrakturMaguntia", serif; font-size: 26px;
    color: var(--back-text); text-align: center;
    padding-bottom: 4px; border-bottom: 1px solid var(--back-text);
  }
</style>
</head>
<body>
<main class="canvas">

  <section class="card card-front" aria-label="Business card front">
    <svg class="cert-badge" width="110" height="50" viewBox="0 0 110 50" aria-hidden="true">
      <circle cx="24" cy="25" r="22" fill="none" stroke="var(--badge)" stroke-width="2"/>
      <circle cx="24" cy="25" r="15" fill="var(--badge)"/>
      <rect x="46" y="10" width="60" height="30" fill="none" stroke="var(--badge)" stroke-width="2"/>
    </svg>

    <div class="brand-mark"><span class="mark-square"></span><span>MB&amp;LR</span></div>
    <div class="company-line">Mountain Beam &amp; Load Rigging</div>

    <svg class="anniversary-badge" width="70" height="80" viewBox="0 0 70 80" aria-hidden="true">
      <circle cx="35" cy="32" r="28" fill="none" stroke="var(--badge)" stroke-width="3"/>
      <circle cx="35" cy="32" r="16" fill="var(--badge)"/>
      <rect x="12" y="68" width="46" height="8" fill="var(--badge)"/>
    </svg>

    <div class="contact">
      <div class="person-name">Daniel Hartley</div>
      <div class="person-title">Managing Director</div>
      <div class="address">480 East 200 South Ridgefield City 84120 &nbsp;|&nbsp; <span class="web">www.mbandlr.com</span></div>
      <div class="phones"><b>P:</b> 801.555.0142 &nbsp;|&nbsp; <b>F:</b> 801.555.0187</div>
    </div>
  </section>

  <section class="card card-back" aria-label="Business card back">
    <div class="scene-fill" role="img" aria-label="Dark blue photograph of a welder in protective gear working inside a steel vessel, with smoke"></div>
    <div class="back-title">Mountain Beam &amp; Load Rigging</div>
  </section>

</main>
</body>
</html>
```